Business Card Design Project

We are an incubator company that helps young entrepreneur to launch new ideas into the market. We will be targeting investors or likewise; Angels, young entrepreneurs and technopreneurs.

Our logo is being tasked by artswarm to design, therefore there is no logo for now.
You can us Lanternfield Pte Ltd as the logo for the time being.

Please let us have some versions of modern and yet professional designs; for words, you can indicate e.g (address), (Title)

thanks

Target Market(s)

young entrepreneurs
angels, investors

Industry/Entity Type

Business

Colors
3176b5
ffffff

Requirements
Must have
• able to project out our name; Lanternfield
Should not have
• Nothing childish or cartoon

```html
<!DOCTYPE html>
<html lang="en">
<head>
<meta charset="utf-8">
<title>Lanternfield Business Card</title>
<link href="https://fonts.googleapis.com/css2?family=Ubuntu:wght@400;500;700&family=Arimo:wght@400&display=swap" rel="stylesheet">
<style>
  :root {
    --bg: #d9d7dc;
    --blue-light: #2c73b3;
    --blue-mid: #1a4f84;
    --blue-deep: #0d3561;
    --card-white: #f4f4f5;
    --ink-blue: #1f6cb0;
    --silver: #cfd3d8;
  }
  * { margin: 0; padding: 0; box-sizing: border-box; }
  html, body {
    width: 1200px; height: 900px; overflow: hidden;
    background: var(--bg);
  }
  .canvas {
    position: relative; width: 1200px; height: 900px;
    display: flex; align-items: center; justify-content: center; gap: 60px;
  }
  .card {
    position: relative; width: 500px; height: 284px; overflow: hidden;
    box-shadow: 3px 4px 10px rgba(0,0,0,0.35);
  }
  .card-front {
    background: radial-gradient(ellipse at 50% 38%, var(--blue-light) 0%, var(--blue-mid) 55%, var(--blue-deep) 100%);
    display: flex; align-items: center; justify-content: center;
  }
  .brand {
    display: flex; align-items: center; gap: 14px;
    font-family: "Ubuntu", sans-serif; font-weight: 700;
    font-size: 32px; letter-spacing: 1px; color: var(--silver);
    text-transform: uppercase;
  }
  .brand-dot {
    width: 22px; height: 22px; border-radius: 50%; background: var(--silver);
  }
  .card-back { background: var(--card-white); }
  .card-back-shapes { position: absolute; inset: 0; width: 100%; height: 100%; display: block; }
  .contact {
    position: absolute; left: 207px; top: 88px;
    color: var(--ink-blue);
  }
  .contact-name {
    font-family: "Ubuntu", sans-serif; font-weight: 400;
    font-size: 28px; line-height: 34px; margin-bottom: 8px; white-space: nowrap;
  }
  .contact-list { list-style: none; font-family: "Arimo", sans-serif; font-size: 12px; }
  .contact-list li { display: flex; align-items: center; gap: 8px; height: 23px; white-space: nowrap; }
  .contact-icon { width: 14px; height: 14px; flex: none; fill: var(--ink-blue); display: block; }
</style>
</head>
<body>
<main class="canvas">
  <section class="card card-front" aria-label="Card front">
    <div class="brand"><span class="brand-dot"></span><span>Lanternfield</span></div>
  </section>

  <section class="card card-back" aria-label="Card back">
    <svg class="card-back-shapes" viewBox="0 0 500 284" preserveAspectRatio="none" aria-hidden="true">
      <defs>
        <linearGradient id="paper" x1="0" y1="0" x2="1" y2="1">
          <stop offset="0" stop-color="#f7f7f8"/>
          <stop offset="1" stop-color="#e2e2e4"/>
        </linearGradient>
      </defs>
      <rect width="500" height="284" fill="url(#paper)"/>
      <polygon points="0,0 166,0 40,208 185,284 0,284" fill="#12487a"/>
      <polygon points="0,222 40,208 185,284 0,284" fill="#0c2f55"/>
    </svg>
    <div class="contact">
      <p class="contact-name">Name Surname</p>
      <ul class="contact-list">
        <li><svg class="contact-icon" viewBox="0 0 16 16"><path d="M3 1l3 3-1.5 2c1 2 2.5 3.5 4.5 4.5L11 9l3 3-2 2.5C6.5 14 2 9.5 1.5 3z"/></svg>000 000 000</li>
        <li><svg class="contact-icon" viewBox="0 0 16 16"><path d="M4 0h8a1 1 0 011 1v14a1 1 0 01-1 1H4a1 1 0 01-1-1V1a1 1 0 011-1zm1 2v10h6V2z"/></svg>000 000 000</li>
        <li><svg class="contact-icon" viewBox="0 0 16 16"><path d="M1 3h14v1L8 9 1 4zm0 3l7 5 7-5v7H1z"/></svg>email@website.com</li>
        <li><svg class="contact-icon" viewBox="0 0 16 16"><path d="M8 1a7 7 0 100 14A7 7 0 008 1zm0 1.5c.8 0 1.7 1.6 2 4H6c.3-2.4 1.2-4 2-4zM2.6 7.5h2.4c0-1.5.3-2.9.8-3.9A5.5 5.5 0 002.6 7.5zm8.4 0h2.4a5.5 5.5 0 00-3.2-3.9c.5 1 .8 2.4.8 3.9zM2.6 8.5a5.5 5.5 0 003.2 3.9c-.5-1-.8-2.4-.8-3.9zm3.4 0c.1 2.4 1.1 4 2 4s1.9-1.6 2-4zm5 0c0 1.5-.3 2.9-.8 3.9a5.5 5.5 0 003.2-3.9z"/></svg>www.website.com</li>
      </ul>
    </div>
  </section>
</main>
</body>
</html>
```